Ground breaking athletic gear company needs a kick ass business card

We are an American start up athletic gear company that uses a medically proven biohack to boost athletic performance. Heat kills strength and endurance. Our gear helps athletes manage heat better and ultimatley can improve them by up to 10% instantly. Nothing like it out there! Launching this summer.
We are looking for a modern, minimalist design that captures a sporty edge. Check out www.velmarunwear.com, @velmarunwear on instagram for more ideas.

Target Market(s)

25-35 year olds, male and female athletes, vaultlift athletes, competitive runners

Industry/Entity Type

Business

Contact Information for Business Card

Dorian Pellham
Founder
dorianp@velmarunwear.com
www.VelmaRunwear.com
+1 (555) 014-2286

Font styles to use
Sans Serif

Requirements
Must have
• Logo and icon
• All contact information
• dorianp@velmarunwear.com
• +1 (555) 019-4471 M
• +1 (555) 014-2286
Nice to have
• Tag line : "Chill & Charge"

```html
<!DOCTYPE html>
<html lang="en">
<head>
<meta charset="utf-8">
<title>Velma Runwear — Business Card</title>
<link rel="stylesheet" href="https://fonts.googleapis.com/css2?family=Open+Sans:ital,wght@0,400;0,600;1,400&family=Jost:ital,wght@1,400&display=swap">
<style>
  :root {
    --stage: #5b4a3d;
    --card-white: #ffffff;
    --card-black: #000000;
    --ink: #111111;
    --ink-soft: #3a3a3a;
    --rule: #222222;
    --band-black: #000000;
    --band-grey: #9a9a9a;
    --paper-text: #ffffff;
  }
  * { margin: 0; padding: 0; box-sizing: border-box; }
  html, body { width: 1200px; height: 987px; overflow: hidden; }
  body {
    background: var(--stage);
    position: relative;
    font-family: "Open Sans", Arial, sans-serif;
    color: var(--ink);
  }
  .card {
    position: absolute;
    left: 293px;
    width: 615px;
    height: 351px;
    overflow: hidden;
  }
  .card--front { top: 130px; background: var(--card-white); }
  .card--back  { top: 505px; background: var(--card-black); }

  .brand-name {
    position: absolute;
    right: 41px;
    top: 98px;
    font-size: 18px;
    font-weight: 600;
    letter-spacing: 3px;
    text-transform: uppercase;
    color: var(--ink);
  }
  .holder { position: absolute; left: 32px; top: 193px; }
  .holder__name { font-size: 22px; font-weight: 600; line-height: 28px; }
  .holder__role { font-size: 16px; line-height: 20px; color: var(--ink-soft); }
  .rule {
    position: absolute; left: 32px; right: 41px; top: 251px;
    height: 1px; background: var(--rule);
  }
  .contacts { position: absolute; left: 32px; top: 263px; list-style: none; }
  .contacts li {
    display: flex; align-items: center; gap: 9px;
    font-size: 15.5px; line-height: 23px; color: var(--ink-soft);
  }
  .contacts svg { width: 14px; height: 16px; flex: none; }
  .website {
    position: absolute; right: 41px; top: 284px;
    font-size: 16px; font-style: italic; letter-spacing: 1.4px; color: var(--ink-soft);
  }
  .band { position: absolute; left: 0; bottom: 0; width: 615px; height: 14px; }

  .back-pattern { position: absolute; inset: 0; }
  .back-brand {
    position: absolute; right: 41px; top: 238px;
    font-size: 18px; font-weight: 600; letter-spacing: 3px;
    text-transform: uppercase; color: var(--paper-text);
  }
  .tagline {
    position: absolute; right: 41px; top: 300px;
    font-family: "Jost", "Futura", Arial, sans-serif;
    font-style: italic; font-size: 18px; color: var(--paper-text);
  }
</style>
</head>
<body>

<section class="card card--front" aria-label="Business card front">
  <div class="brand-name">Velma Runwear</div>

  <div class="holder">
    <div class="holder__name">Dorian Pellham</div>
    <div class="holder__role">Founder</div>
  </div>

  <div class="rule"></div>

  <ul class="contacts">
    <li>
      <svg viewBox="0 0 14 16" aria-hidden="true">
        <rect x="3" y="1" width="8" height="14" rx="1.5" fill="none" stroke="#111" stroke-width="1.6"/>
        <rect x="5" y="3" width="4" height="8" fill="#111"/>
      </svg>
      +1 (555) 014-2286
    </li>
    <li>
      <svg viewBox="0 0 14 16" aria-hidden="true">
        <rect x="1" y="4" width="12" height="8" fill="#111"/>
        <path d="M1 4 L7 9 L13 4" fill="none" stroke="#fff" stroke-width="1.2"/>
      </svg>
      dorianp@velmarunwear.com
    </li>
  </ul>

  <div class="website">www.VelmaRunwear.com</div>

  <svg class="band" viewBox="0 0 615 14" preserveAspectRatio="none" aria-hidden="true">
    <polygon points="0,0 400,0 396,14 0,14" fill="#000"/>
    <polygon points="405,0 615,0 615,14 401,14" fill="#9a9a9a"/>
  </svg>
</section>

<section class="card card--back" aria-label="Business card back">
  <svg class="back-pattern" viewBox="0 0 615 351" preserveAspectRatio="none" role="img" aria-label="Faint repeating chevron pattern across the card back">
    <defs>
      <linearGradient id="patternTone" x1="0" y1="0" x2="0" y2="1">
        <stop offset="0" stop-color="#0d0d0d"/>
        <stop offset="1" stop-color="#030303"/>
      </linearGradient>
    </defs>
    <rect width="615" height="351" fill="url(#patternTone)"/>
  </svg>
  <div class="back-brand">Velma Runwear</div>
  <div class="tagline">Chill &amp; Charge</div>
</section>

</body>
</html>
```